Fitness blog needs business cards

Seeking a designer that can interpret words and put them into visual design.

I am a personal trainer with a fitness blog that showcases my own recipes and fitness tips. Currently in the process of creating various ebooks with workouts and recipe books which will be marketed under my brand "Falcon Striver".

Looking to have my current website www.mirandatollen.example promoted with my name, email and phone number plus with my other business/brand "Falcon Striver".

These business cards are to give out to potential investors, business partners, clients and collaborators to provide an overview of what I do, my mission / vision and my business. My passion has to come through in the cards and has to blow their socks off.

Seeking to work with someone long term that can also assist with designs of web banners, ebook designs and other artwork in the near future.

Please refer to attachments for inspo and logos and colours.

Target Market(s)

20-50 year old males and females
everyday people that want to get fit and feel better

Industry/Entity Type

Health And Wellness

Contact Information for Business Card

Miranda Tollen
+61 4 83 562 048
miranda@mirandatollen.example
www.mirandatollen.example

Font styles to use
Other font styles liked:
• Montserrat, Vollkorn, See logos attached.

Colors
f78f20
faa54b
0293ce
33a6d7
f68d4c
f9ba93
fcca95

Requirements
Must have
• Business cards must display my contact details and should be focused on the customer, it should not be too much about me. My passion for health and wellbeing needs to pop out. I want to help others get fit and make a difference in people's lives by getting them to move more and sit less. I don't want people to be like fitness models I want them to simply feel better than yesterday.
Nice to have
• Please refer to attached images that have logo and colours already designed. Nice and clean design.
Should not have
• Business cards should not be too busy. I like a clean design.

```html
<!DOCTYPE html>
<html lang="en">
<head>
<meta charset="utf-8">
<title>Miranda Tollen – Business Cards</title>
<link rel="stylesheet" href="https://fonts.googleapis.com/css2?family=Montserrat:wght@400;500;600;700&display=swap">
<style>
  :root {
    --stage: #3b3b3d;
    --card-white: #ffffff;
    --orange: #f78f20;
    --orange-soft: #e2a865;
    --blue: #0293ce;
    --blue-light: #33a6d7;
    --ink: #1c1c1c;
    --photo-dark: #3a2416;
    --photo-mid: #8a4f26;
    --photo-warm: #a9622f;
    --photo-light: #f3ece4;
    --sand: #e8d3b4;
  }
  * { box-sizing: border-box; margin: 0; padding: 0; }
  html, body {
    width: 1200px; height: 900px; overflow: hidden;
    background: var(--stage);
    font-family: "Montserrat", sans-serif;
  }
  .canvas { position: relative; width: 1200px; height: 900px; }
  .card {
    position: absolute; left: 250px; width: 700px; height: 400px;
    overflow: hidden; background: var(--card-white);
    box-shadow: 0 12px 30px rgba(0,0,0,.45);
  }
  .card--front { top: 40px; }
  .card--back { top: 460px; }

  /* Front */
  .front-photo {
    position: absolute; inset: 0;
    background:
      radial-gradient(ellipse 340px 210px at 80% 10%, #ffffff 0%, var(--photo-light) 35%, rgba(243,236,228,0) 100%),
      linear-gradient(90deg, var(--photo-dark) 0%, var(--photo-mid) 40%, var(--photo-warm) 100%);
  }
  .brand-box {
    position: absolute; left: 235px; top: 120px;
    display: flex; align-items: center; gap: 10px;
    padding: 12px 22px; background: #ffffff;
  }
  .brand-box__mark { width: 12px; height: 12px; background: var(--blue); }
  .brand-box__name {
    font-weight: 500; font-size: 18px; letter-spacing: 6px; color: var(--ink);
  }
  .tagline {
    position: absolute; left: 255px; top: 225px;
    color: #ffffff; text-transform: uppercase; line-height: 1.1;
    text-shadow: 0 1px 3px rgba(0,0,0,.25);
  }
  .tagline__small { font-size: 15px; font-weight: 500; letter-spacing: 1px; }
  .tagline__big { font-size: 24px; font-weight: 700; color: var(--orange-soft); }

  /* Back */
  .back-photo {
    position: absolute; left: 0; top: 0; width: 330px; height: 400px;
    background: linear-gradient(180deg, #f4f6f7 0%, #e9ecee 55%, var(--sand) 85%, #caa77c 100%);
  }
  .back-photo__post {
    position: absolute; left: 30px; top: 40px; width: 38px; height: 360px;
    background: #a88a66;
  }
  .back-brand {
    position: absolute; left: 365px; top: 62px;
    display: flex; align-items: center; gap: 12px;
  }
  .back-brand__mark { width: 14px; height: 14px; background: var(--orange); }
  .back-brand__name {
    font-size: 20px; font-weight: 500; letter-spacing: 6px; color: var(--ink);
    text-transform: uppercase; white-space: nowrap;
  }
  .contact {
    position: absolute; left: 340px; top: 170px; width: 330px; text-align: right;
  }
  .contact__name {
    font-size: 25px; font-weight: 700; color: var(--orange-soft);
    text-transform: uppercase; margin-bottom: 14px;
  }
  .contact__line { font-size: 17px; font-weight: 500; color: var(--ink); margin-bottom: 6px; }
  .contact__web { font-size: 17px; font-weight: 500; color: var(--blue-light); }
</style>
</head>
<body>
<main class="canvas">
  <section class="card card--front">
    <div class="front-photo" role="img" aria-label="Sunlit photo of a trainer on the beach shaping a heart with her hands"></div>
    <div class="brand-box">
      <span class="brand-box__mark"></span>
      <span class="brand-box__name">MIRANDA TOLLEN</span>
    </div>
    <div class="tagline">
      <p class="tagline__small">Your guide to</p>
      <p class="tagline__big">Get fitter</p>
      <p class="tagline__big">Stronger &amp; healthier</p>
      <p class="tagline__small">Than yesterday</p>
    </div>
  </section>

  <section class="card card--back">
    <div class="back-photo" role="img" aria-label="Photo of a fit woman posing by a wooden post on a sunny beach">
      <div class="back-photo__post"></div>
    </div>
    <div class="back-brand">
      <span class="back-brand__mark"></span>
      <span class="back-brand__name">Falcon Striver</span>
    </div>
    <div class="contact">
      <p class="contact__name">Miranda Tollen</p>
      <p class="contact__line">+61 4 83 562 048</p>
      <p class="contact__line">miranda@mirandatollen.example</p>
      <p class="contact__web">www.mirandatollen.example</p>
    </div>
  </section>
</main>
</body>
</html>
```